Online ticketing company needs new biz card design

Needing an updated business card to reflect our company, incorporating our existing logo and colour scheme (red, black, white). The design should communicate our modern, online, technology, innovation based company.

Details for card need to include the following:

Name
Position
Telephone and extension number
Mobile number
Email
Web address
Physical and/or postal address

Industry/Entity Type

Business

Font styles to use
Sans Serif

Requirements
Must have
• Clear, bold, eye catching design

```html
<!DOCTYPE html>
<html lang="en">
<head>
<meta charset="utf-8">
<title>Gatelane Business Card</title>
<link href="https://fonts.googleapis.com/css2?family=Nunito+Sans:wght@400;600;800&display=swap" rel="stylesheet">
<style>
  :root {
    --bg: #e4e4e4;
    --card-black: #141414;
    --card-white: #ffffff;
    --brand-red: #d32027;
    --text-light: #f2f2f2;
    --ink: #111111;
  }
  * { box-sizing: border-box; margin: 0; padding: 0; }
  html, body {
    width: 1200px;
    height: 900px;
    overflow: hidden;
    background: var(--bg);
    font-family: "Nunito Sans", Arial, sans-serif;
  }
  .stage {
    position: relative;
    width: 1200px;
    height: 900px;
    display: flex;
    align-items: center;
    justify-content: center;
    gap: 60px;
  }
  .card {
    position: relative;
    width: 520px;
    height: 300px;
    border-radius: 18px;
    overflow: hidden;
    background: var(--card-black);
    box-shadow: 0 14px 28px rgba(0,0,0,0.22);
  }
  .card-shapes {
    position: absolute;
    inset: 0;
  }
  .contact-block {
    position: absolute;
    left: 40px;
    top: 78px;
    color: var(--text-light);
  }
  .person-name {
    color: var(--brand-red);
    font-size: 21px;
    font-weight: 600;
    margin-left: 28px;
    line-height: 1.1;
  }
  .person-role {
    font-size: 15px;
    margin-left: 36px;
    margin-bottom: 24px;
  }
  .contact-list { list-style: none; }
  .contact-list li {
    display: flex;
    align-items: center;
    gap: 5px;
    font-size: 14px;
    line-height: 19px;
  }
  .contact-list li.continued { padding-left: 17px; }
  .contact-icon { width: 12px; height: 12px; flex: none; fill: var(--brand-red); }
  .front-wordmark {
    position: absolute;
    left: 270px;
    right: 10px;
    top: 0;
    bottom: 0;
    display: flex;
    align-items: center;
    justify-content: center;
    font-size: 46px;
    font-weight: 800;
    color: var(--ink);
    letter-spacing: 1px;
  }
  .back-wordmark {
    position: absolute;
    inset: 0;
    display: flex;
    align-items: center;
    justify-content: center;
    font-size: 54px;
    font-weight: 800;
    color: var(--brand-red);
    letter-spacing: 1px;
  }
</style>
</head>
<body>
<main class="stage">
  <section class="card card-front">
    <svg class="card-shapes" viewBox="0 0 520 300" preserveAspectRatio="none" aria-hidden="true">
      <path d="M212 0 L258 0 C198 60 190 140 204 215 C184 140 182 60 212 0 Z" fill="var(--brand-red)"/>
      <path d="M252 0 L520 0 L520 300 L300 300 C205 250 190 80 252 0 Z" fill="var(--card-white)"/>
    </svg>
    <div class="contact-block">
      <h1 class="person-name">Marcus Vale</h1>
      <p class="person-role">Manager</p>
      <ul class="contact-list">
        <li><svg class="contact-icon" viewBox="0 0 12 12"><path d="M2 1 L4.5 1 L5.5 3.5 L4 4.5 C4.8 6.2 5.8 7.2 7.5 8 L8.5 6.5 L11 7.5 L11 10 C6 10.5 1.5 6 2 1 Z"/></svg>555.214.3380 Ext 210</li>
        <li><svg class="contact-icon" viewBox="0 0 12 12"><rect x="3" y="0.5" width="6" height="11" rx="1"/><rect x="4" y="2" width="4" height="6" fill="var(--card-black)"/></svg>555.309.7712</li>
        <li><svg class="contact-icon" viewBox="0 0 12 12"><circle cx="6" cy="6" r="5" fill="none" stroke="var(--brand-red)" stroke-width="1.2"/><ellipse cx="6" cy="6" rx="2" ry="5" fill="none" stroke="var(--brand-red)" stroke-width="1"/><path d="M1 6 H11" stroke="var(--brand-red)" stroke-width="1"/></svg>www.gatelane.com</li>
        <li><svg class="contact-icon" viewBox="0 0 12 12"><rect x="0.5" y="2.5" width="11" height="7.5" rx="1"/><path d="M1 3 L6 7 L11 3" fill="none" stroke="var(--card-black)" stroke-width="1"/></svg>hello@gatelane.com</li>
        <li><svg class="contact-icon" viewBox="0 0 12 12"><path d="M6 1 L11.5 6 L10 6 L10 11 L7.5 11 L7.5 8 L4.5 8 L4.5 11 L2 11 L2 6 L0.5 6 Z"/></svg>418 Cedar Mill Lane</li>
        <li class="continued">Fairview, GA 30127</li>
      </ul>
    </div>
    <div class="front-wordmark">Gatelane</div>
  </section>

  <section class="card card-back">
    <div class="back-wordmark">Gatelane</div>
  </section>
</main>
</body>
</html>
```